Redesign of 15 emails for a Software Company

Hello and welcome to our project. We are in need of a designer to create 15 different emails in HTML that one of our software programs uses. I’ve attached the 15 emails for your review. These emails were created about 4 years ago and are outdated as far as design/ style / font etc is concerned.

FOR THE CONTEST, WE WOULD LIKE YOU TO CREATE AN EMAIL FOR #1 (01 Welcome Email - Buyer and Seller) If you are able to do a second email that would be great so that we can have an idea of what the others will look like. Based on these designs (we will pick the best one) to do all 15 emails.

Must be HTML

DESIGN / FEEL
We are looking to have these emails totally refreshed. We are looking for a much more modern and cleaner feel. More like how Velmo does their emails etc.

COLORS
Colors to be mostly greys and whites (neutral colors).

UNIFORMITY
Although each email will have its own attributes, we would like a common theme for all the emails.

***Please use new Zorbiks ... Krims... equpiment
***Also we included a screenshot of an email template that we found on the internet that we like. We uploaded it to "Look and Feel Sliders" for a frame of reference.

Font styles to use
Sans Serif

Requirements
Must have
• New KRIMS or Computers .. modern font ... neutral colors -- grey.white etc

```html
<!DOCTYPE html>
<html lang="en">
<head>
<meta charset="utf-8">
<title>Welcome to the Digital Closing Package</title>
<link rel="stylesheet" href="https://fonts.googleapis.com/css2?family=Montserrat:wght@400;500;600;700&family=Poppins:wght@300;400;500;600&family=Baloo+2:wght@500;600&display=swap">
<style>
:root{
  --bar:#6f8ca4;
  --white:#ffffff;
  --grey-band:#efefef;
  --blush:#fdf9f7;
  --mint:#ecf3f2;
  --steel:#7a9ebe;
  --ink:#2b2b2b;
  --text:#3d3d3d;
  --muted:#555;
  --icon:#454545;
  --ring:#9a9a9a;
}
*{margin:0;padding:0;box-sizing:border-box}
html,body{width:1200px;height:4968px;overflow:hidden;background:var(--white)}
body{font-family:'Poppins',sans-serif;color:var(--text);position:relative}
.band{position:absolute;left:0;width:1200px}
.abs{position:absolute}
.topbar{top:0;height:74px;background:var(--bar);color:var(--white);font-family:Arial,sans-serif;font-size:21px;text-align:center;line-height:68px}
.header{top:74px;height:200px;background:var(--white)}
.brand{left:164px;top:62px;font-family:'Montserrat',sans-serif;font-weight:600;font-size:52px;color:var(--ink);display:flex;align-items:center;gap:16px}
.brand-dot{width:22px;height:22px;border-radius:50%;background:var(--ink)}
.contact{left:743px;top:32px;font-family:'Montserrat',sans-serif;font-size:23px;line-height:25.5px;color:var(--ink);letter-spacing:.5px}
.contact b{font-weight:600}
.contact .gap{height:14px}
.hero{top:274px;height:1130px;background:var(--grey-band)}
.h-title{width:100%;text-align:center;font-family:'Montserrat',sans-serif;font-weight:600;color:var(--ink)}
.hero .h-title{top:47px;font-size:38px}
.hero-sub{width:100%;top:122px;text-align:center;font-family:'Montserrat',sans-serif;font-size:28px;line-height:33px;color:var(--muted)}
.hero-visual{left:289px;top:266px;width:627px;height:781px;border-radius:60px;background:linear-gradient(160deg,#e2e4e6,#c9cdd1 55%,#dfe1e3)}
.letter{top:1404px;height:535px;background:var(--blush)}
.letter-body{left:199px;top:80px;width:840px;font-size:22.5px;line-height:33px;color:var(--text)}
.letter-body .greet{font-family:'Montserrat',sans-serif;font-weight:600;font-size:27px;margin-bottom:22px;color:var(--ink)}
.letter-body p{margin-bottom:16px}
.preclose{top:1939px;height:852px;background:var(--mint)}
.section-title{width:100%;text-align:center;font-family:'Montserrat',sans-serif;font-weight:600;font-size:37px;color:var(--ink)}
.section-sub{width:100%;text-align:center;font-family:'Montserrat',sans-serif;font-size:28px;color:var(--muted);letter-spacing:.5px}
.feature-icon{width:158px;height:158px}
.feature-head{font-family:'Montserrat',sans-serif;font-weight:700;font-size:25px;line-height:33px;letter-spacing:1.5px;color:var(--ink)}
.feature-text{font-size:22px;line-height:31px;color:var(--text)}
.bullets{list-style:none}
.bullets li{position:relative;padding-left:22px;margin-bottom:5px}
.bullets li::before{content:"";position:absolute;left:0;top:11px;width:11px;height:11px;border-radius:50%;background:var(--icon)}
.postclose{top:2791px;height:938px;background:var(--blush)}
.tablet-visual{left:247px;top:193px;width:708px;height:382px;border-radius:20px;background:linear-gradient(180deg,#e9ecef,#cfd5db 60%,#e4e6e8);border:12px solid #1e1e1e}
.video{top:3729px;height:685px;background:var(--steel)}
.video-frame{left:179px;top:110px;width:805px;height:399px;border-radius:70px;border:16px solid #222;background:linear-gradient(120deg,#cfd3d6,#9fa6ac 50%,#c6cacd);overflow:hidden}
.play{left:368px;top:143px;width:72px;height:72px}
.video-title{width:100%;top:548px;text-align:center;font-family:'Baloo 2',sans-serif;font-weight:600;font-size:52px;color:var(--white);letter-spacing:1px}
.profile{top:4414px;height:362px;background:var(--mint)}
.avatar{left:178px;top:46px;width:262px;height:262px}
.profile-title{left:525px;top:50px;font-family:'Montserrat',sans-serif;font-weight:600;font-size:38px;color:var(--ink)}
.profile-text{left:525px;top:128px;width:520px;font-size:23px;line-height:33px;color:var(--text)}
.profile-link{left:525px;top:258px;font-family:'Montserrat',sans-serif;font-weight:500;font-size:27px;color:var(--ink);text-decoration:underline;text-underline-offset:8px}
.footer{top:4776px;height:192px;background:var(--white);text-align:center;font-family:Arial,sans-serif;font-size:20px;color:var(--ink)}
.footer p{position:absolute;width:100%}
.footer a{color:var(--ink);font-weight:700;text-decoration:underline}
</style>
</head>
<body>

<div class="band topbar">Don't see this email properly? View in web browser</div>

<header class="band header">
  <div class="abs brand"><span class="brand-dot"></span>Fernway</div>
  <div class="abs contact">
    Lindenkade 24, 4100 KR<br>Oosterveld, 204817
    <div class="gap"></div>
    <b>P:</b> 5550 .0199.2041<br>
    <b>E:</b> hello@fernway.com<br>
    <b>W:</b>www.fernway.com
  </div>
</header>

<section class="band hero">
  <h1 class="abs h-title">Welcome to the Digital Closing Package</h1>
  <p class="abs hero-sub">Committed to keeping you informed<br>during every step pf the closing process</p>
  <div class="abs hero-visual" role="img" aria-label="Two smartphones showing a map and the closing timeline screen"></div>
</section>

<section class="band letter">
  <div class="abs letter-body">
    <p class="greet">Dear {%CLIENT%},</p>
    <p>On behalf of all us at {%TITLECOMPANY%}, we look forward to a succesful closing.</p>
    <p>As we at {%TITLECOMPANY%} think it is important to keep all parties involved in a real estate transaction properly informed of the progress, we have implemented the innovative Digital Closing Package to keep everyone on the same page.</p>
    <p><strong>Please Note:</strong> You will receive another email with instructions on how to create your user account.</p>
  </div>
</section>

<section class="band preclose">
  <h2 class="abs section-title" style="top:62px">Pre-Close</h2>
  <p class="abs section-sub" style="top:122px">Features &amp; Benefits</p>

  <svg class="abs feature-icon" style="left:170px;top:256px" viewBox="0 0 158 158" aria-hidden="true">
    <circle cx="79" cy="79" r="77" fill="#fff" stroke="var(--ring)" stroke-width="2"/>
    <path d="M40 113 L66 80 L76 92 L88 74 L118 113 Z" fill="var(--icon)"/>
    <path d="M88 74 V46" stroke="var(--icon)" stroke-width="3"/>
    <path d="M88 46 L104 52 L88 58 Z" fill="var(--icon)"/>
  </svg>
  <svg class="abs feature-icon" style="left:500px;top:256px" viewBox="0 0 158 158" aria-hidden="true">
    <circle cx="79" cy="79" r="77" fill="#fff" stroke="var(--ring)" stroke-width="2"/>
    <rect x="44" y="44" width="40" height="70" rx="5" fill="var(--icon)"/>
    <rect x="50" y="54" width="28" height="46" fill="#fff"/>
    <rect x="66" y="58" width="50" height="34" rx="5" fill="var(--icon)"/>
    <path d="M74 92 L74 104 L86 92 Z" fill="var(--icon)"/>
    <rect x="74" y="66" width="34" height="4" fill="#fff"/>
    <rect x="74" y="75" width="26" height="4" fill="#fff"/>
  </svg>
  <svg class="abs feature-icon" style="left:783px;top:256px" viewBox="0 0 158 158" aria-hidden="true">
    <circle cx="79" cy="79" r="77" fill="#fff" stroke="var(--ring)" stroke-width="2"/>
    <path d="M46 56 H72 L78 64 H112 V110 H46 Z" fill="var(--icon)"/>
    <path d="M79 76 L90 88 H83 V100 H75 V88 H68 Z" fill="#fff"/>
  </svg>

  <div class="abs" style="left:170px;top:472px;width:260px">
    <div class="feature-head">MILESTONE</div>
    <p class="feature-text" style="margin-top:60px">You will be provided your own dashboard where you can log in to see which stage your transaction is in.</p>
  </div>
  <div class="abs" style="left:502px;top:472px;width:230px">
    <div class="feature-head">SMS - EMAIL<br>MESSAGING</div>
    <p class="feature-text" style="margin-top:27px">The system will also provide you milestone alerts via SMS or email, so you always know the status of your transaction.</p>
  </div>
  <div class="abs" style="left:783px;top:472px;width:280px">
    <div class="feature-head">OTHER<br>FEATURES</div>
    <ul class="feature-text bullets" style="margin-top:27px">
      <li>Secure Wiring Instruc tions</li>
      <li>FAQ of Closing Process</li>
      <li>Document Sharing</li>
      <li>Moving Checklist</li>
      <li>Moving Wishlist</li>
    </ul>
  </div>
</section>

<section class="band postclose">
  <h2 class="abs section-title" style="top:30px">Post-Close</h2>
  <p class="abs section-sub" style="top:93px">Features &amp; Benefits</p>
  <div class="abs tablet-visual" role="img" aria-label="Tablet showing the transaction dashboard with map, mortgage rate chart and contact cards"></div>

  <div class="abs" style="left:166px;top:650px;width:420px">
    <div class="feature-head">YOUR CLOSING DOCUMENTS<br>SECURELY HOSTED</div>
    <p class="feature-text" style="margin-top:34px">After closing, all of your important closing documents will be securely hosted for your access 24X7X365.</p>
  </div>
  <div class="abs" style="left:631px;top:650px;width:420px">
    <div class="feature-head">STORE ALL OTHER REAL ESTATE<br>RELATED DOCUMENTS</div>
    <p class="feature-text" style="margin-top:34px">You can upload documents that pertain to your property so every-thing is one place when you need it in the future.</p>
  </div>
</section>

<section class="band video">
  <div class="abs video-frame" role="img" aria-label="Introduction video still of a presenter in a modern office">
    <svg class="abs play" viewBox="0 0 72 72" aria-hidden="true">
      <rect width="72" height="72" fill="#fff"/>
      <circle cx="36" cy="36" r="26" fill="#e8452c"/>
      <path d="M29 23 L50 36 L29 49 Z" fill="#fff"/>
    </svg>
  </div>
  <h2 class="abs video-title">Watch Introduction Video</h2>
</section>

<section class="band profile">
  <svg class="abs avatar" viewBox="0 0 262 262" aria-hidden="true">
    <circle cx="131" cy="131" r="131" fill="#2f2f2f"/>
    <circle cx="131" cy="131" r="113" fill="#8c8c8c"/>
    <circle cx="131" cy="100" r="40" fill="#2f2f2f"/>
    <path d="M62 190 C70 150 100 142 131 142 C162 142 192 150 200 190 Z" fill="#2f2f2f"/>
  </svg>
  <h2 class="abs profile-title">Edit Profile</h2>
  <p class="abs profile-text">If you wish to edit your profile such as conatct information and /or picture , please click on the following link.</p>
  <a class="abs profile-link" href="#">Edit Your Profile</a>
</section>

<footer class="band footer">
  <p style="top:47px">© 2020, Your Company Name</p>
  <p style="top:80px">Don't want to receive email. please change your <a href="#">preference</a> or <a href="#">unsubscribe</a> us.</p>
</footer>

</body>
</html>
```